Startup Management Consultancy needs Company 1st birthday card

We need a card design to keep interest in our new company based in Newcastle, NSW but whose customers are Australia-wide, particularly Operations Managers, CEOs and company owners. We are a company who deal with the top decision makers of a company but who do most of our work on the factory floor finding gaps and improving the productivity of complex process which always involve people. Our company colours are pantone 288 and white and we have used some printed material with blue backgrounds. We want to communicate our professionalism, a high quality service, elegance and a touch of celebration for our 1st birthday.

Target Market(s)

35-45 years old, generally, males either operations managers, CEOs or company owners, mixed backgrounds, university educated

Industry/Entity Type

It Company

Requirements
Must have
• our logo
our company name in Monotype Corsiva
our text
Nice to have
• Match our previous brochures
show how connected we have been able to become within the short 12 months we have been around

```html
<!DOCTYPE html>
<html lang="en">
<head>
<meta charset="utf-8">
<title>Marlow Advisory – First Birthday Card</title>
<link rel="stylesheet" href="https://fonts.googleapis.com/css2?family=Cormorant+Garamond:ital,wght@1,500;1,600&family=PT+Sans&family=Kalam&display=swap">
<style>
  :root {
    --navy-deep: #050f26;
    --navy: #0b2a66;
    --royal: #1a4fa3;
    --brand-blue: #0a3b8c;
    --white: #ffffff;
    --balloon-teal: rgba(95, 211, 180, 0.38);
    --balloon-pale: rgba(201, 238, 245, 0.30);
    --footer-bg: #ffffff;
  }
  * { box-sizing: border-box; margin: 0; padding: 0; }
  html, body {
    width: 1200px;
    height: 900px;
    overflow: hidden;
    background: #eeeeee;
  }
  .card {
    position: relative;
    width: 1200px;
    height: 900px;
    display: flex;
    flex-direction: column;
  }
  .card-face {
    position: relative;
    flex: 1;
    background:
      radial-gradient(ellipse 60% 55% at 78% 18%, var(--royal) 0%, transparent 70%),
      radial-gradient(ellipse 55% 60% at 20% 45%, #123f8a 0%, transparent 75%),
      linear-gradient(180deg, var(--navy) 0%, #082056 55%, var(--navy-deep) 100%);
  }
  .balloon-art {
    position: absolute;
    left: 40px;
    top: 50px;
    width: 420px;
    height: 700px;
    background:
      radial-gradient(ellipse 50% 30% at 50% 24%, var(--balloon-pale) 0%, var(--balloon-teal) 45%, transparent 100%),
      radial-gradient(ellipse 35% 55% at 50% 62%, rgba(95, 211, 180, 0.14) 0%, transparent 100%);
  }
  .message {
    position: absolute;
    left: 480px;
    top: 0;
    width: 668px;
    color: var(--white);
  }
  .headline {
    margin-top: 48px;
    text-align: center;
    font-family: "Cormorant Garamond", serif;
    font-style: italic;
    font-weight: 600;
    font-size: 54px;
    line-height: 58px;
    padding-left: 20px;
  }
  .salutation {
    margin-top: 30px;
    text-align: center;
    font-family: "Kalam", cursive;
    font-size: 21px;
    line-height: 30px;
    padding-left: 30px;
  }
  .body-copy {
    font-family: "PT Sans", sans-serif;
    font-size: 18.5px;
    line-height: 27px;
    text-align: justify;
  }
  .body-copy p:first-child { margin-top: 16px; }
  .body-copy p + p { margin-top: 27px; }
  .sign-off {
    margin-top: 30px;
    text-align: center;
    font-family: "Kalam", cursive;
    font-size: 21px;
    padding-left: 20px;
  }
  .footer-band {
    height: 100px;
    background: var(--footer-bg);
    display: flex;
    align-items: center;
    color: var(--brand-blue);
  }
  .brand-name {
    display: flex;
    align-items: center;
    gap: 10px;
    margin-left: 48px;
    width: 195px;
    font-family: "Cormorant Garamond", serif;
    font-style: italic;
    font-weight: 600;
    font-size: 30px;
  }
  .brand-dot {
    width: 26px;
    height: 26px;
    border-radius: 50%;
    background: var(--brand-blue);
  }
  .tagline {
    font-family: "Cormorant Garamond", serif;
    font-style: italic;
    font-weight: 600;
    font-size: 36px;
    white-space: nowrap;
  }
</style>
</head>
<body>
<main class="card">
  <section class="card-face">
    <div class="balloon-art" role="img" aria-label="Illustration of a bunch of glossy translucent teal and white balloons with curling ribbons, bubbles and small stars"></div>

    <div class="message">
      <h1 class="headline">Marlow Advisory<br>is turning one!</h1>
      <p class="salutation">Dear Marcus,</p>
      <div class="body-copy">
        <p>We are very excited to have reached such an important milestone in our company and as you were in some way an important part of this, we wanted to share some of our results. We have achieved our set goals for our first year of business, building up a network of partners and potential clients. Our experience and achievements opened doors to some quality smaller boutique consultancies and to a large scale consultancy that will partner with us on bigger projects. We are working hand in hand with industry groups to offer our knowledge to their members and have made many contacts across numerous industries, knowing that it might take years before these contacts turn into engagements. The engagements carried out within our first year have been extremely successful and will serve as excellent references in the future.</p>
        <p>Thank you for taking the time to meet with us, and helping us understand the needs of your industry. We wish you all the best during our next year of business and would be pleased to assist you in any way we can.</p>
      </div>
      <p class="sign-off">Best Regards, Helen, Peter</p>
    </div>
  </section>

  <footer class="footer-band">
    <div class="brand-name"><span class="brand-dot"></span>Marlow</div>
    <p class="tagline">Marlow Advisory, your Key to getting better business results.</p>
  </footer>
</main>
</body>
</html>
```